Web Header needed for an inspirational coaching company's website - ongoing work

We need a beautifully designed web header to replace my current one at my homepage on my website www.brekavol.com
There will be continuous work required for various creative work in the future if your work is selected.
I work with corporate professionals and executives to bring clarity and joy back to their career. It needs to be elegant, sophisticated, intelligent, but friendly and inspiring at the same time.
Brief and the sample header size are attached in my files
Thank you!
Target Market(s)
Corporate profesionals and executives
Industry/Entity Type
It Company
Colors
Designer to choose colors to be used in the design.
Look and feel
Each slider illustrates characteristics of the customer's brand and the style your logo design should communicate.

```html
<!DOCTYPE html>
<html lang="en">
<head>
<meta charset="utf-8">
<title>Clear Horizon – Bring Clarity to Your Career</title>
<link rel="stylesheet" href="https://fonts.googleapis.com/css2?family=Roboto:wght@400;700&family=EB+Garamond:wght@500&family=Mulish:wght@300;400;700&display=swap">
<style>
:root{
  --bar:#222222;
  --white:#ffffff;
  --teal:#1f9785;
  --ink:#555555;
  --ink-strong:#333333;
  --warm-1:#c98a5a;
  --warm-2:#e3b98f;
  --warm-3:#a77a5c;
}
*{box-sizing:border-box;margin:0;padding:0}
html,body{width:1200px;height:1092px;overflow:hidden;background:var(--white)}
body{position:relative;font-family:"Mulish",sans-serif;color:var(--ink)}
.announce{position:absolute;left:0;top:0;width:1200px;height:25px;background:var(--bar);color:var(--white);
  font:400 9.5px/25px "Mulish",sans-serif;letter-spacing:.6px;text-align:center}
.announce-close{position:absolute;right:0;top:0;width:22px;height:25px;background:#111;font-size:9px;line-height:25px;text-align:center}
.hero{position:absolute;left:0;top:25px;width:1200px;height:501px;
  background:radial-gradient(ellipse 380px 420px at 300px 300px,#d9a07a 0%,rgba(217,160,122,0) 100%),
  linear-gradient(100deg,var(--warm-3) 0%,var(--warm-1) 30%,var(--warm-2) 60%,#c9a07c 80%,#b7835e 100%)}
.portrait{position:absolute;left:64px;top:80px;width:336px;height:421px;border-radius:168px 168px 0 0;
  background:linear-gradient(180deg,#3a2a22 0%,#4a3328 40%,#e26a3f 78%,#e86a3b 100%);opacity:.85}
.brand{position:absolute;left:19px;top:16px;color:var(--white);font:400 15px/17px "Roboto",sans-serif;letter-spacing:1px}
.nav{position:absolute;left:490px;top:24px;display:flex;gap:17px;font:400 11.6px/14px "Roboto",sans-serif;color:var(--white)}
.contact{position:absolute;left:1094px;top:17px;width:95px;height:31px;border:1px solid var(--white);border-radius:16px;
  color:var(--white);font:400 12px/29px "Roboto",sans-serif;text-align:center}
.hero-title{position:absolute;left:470px;top:212px;width:585px;text-align:center;color:var(--white);
  font:700 46px/1.1 "Roboto",sans-serif}
.welcome{position:absolute;left:0;top:586px;width:1222px;text-align:center;color:var(--teal);font:500 22px/1 "EB Garamond",serif;letter-spacing:.4px}
.tagline{position:absolute;left:0;top:626px;width:1222px;text-align:center;font:700 11.5px/1 "Mulish",sans-serif;color:var(--ink)}
.clients{position:absolute;left:258px;top:668px;width:710px;height:48px;display:flex;justify-content:space-between;align-items:center;
  font:700 14px/1 "Mulish",sans-serif;color:#666}
.clients span{display:flex;align-items:center;gap:5px}
.clients i{display:inline-block;width:9px;height:9px;background:#888}
.quote{position:absolute;left:0;top:741px;width:1222px;text-align:center;color:var(--teal);font:500 20px/1 "EB Garamond",serif;letter-spacing:.3px}
.story{position:absolute;left:253px;top:791px;width:348px;font:300 12px/18px "Mulish",sans-serif;color:var(--ink);letter-spacing:.1px}
.story p{margin-bottom:12px}
.story a{color:var(--teal);text-decoration:none}
.story .praise{font-weight:700;color:var(--ink-strong)}
.speaker{position:absolute;left:693px;top:791px;width:209px;height:222px;
  background:linear-gradient(160deg,#c9dcf2 0%,#9fc0e8 45%,#e4693f 100%)}
.caption{position:absolute;left:692px;top:1037px;width:205px;font:400 9.6px/13px "Mulish",sans-serif;color:var(--ink);letter-spacing:.2px}
</style>
</head>
<body>
<div class="announce">Discover Your Clear Horizon Workshop - Jul 2 (booked out) OR Aug 6 or Sept 10 | Sydney<span class="announce-close">×</span></div>

<header class="hero">
  <div class="portrait" role="img" aria-label="Portrait photograph of the coach smiling, wearing an orange top"></div>
  <div class="brand">CLEAR<br>HORIZON</div>
  <nav class="nav"><span>Home</span><span>About Mei Lan</span><span>Testimonia</span><span>Methodology</span><span>Coaching &amp; Mentoring</span><span>Workshop</span><span>Corporate</span><span>Blog</span></nav>
  <div class="contact">Contact</div>
  <h1 class="hero-title">Bring Clarity to Your Career</h1>
</header>

<h2 class="welcome">Welcome to Discover You Clear Horizon</h2>
<p class="tagline">A place for professionals &amp; executives to find clarity in their career</p>

<div class="clients">
  <span><i></i>Arvelo</span><span>Quorvin</span><span>Halvex</span><span>Norvale</span><span>Paylume</span><span>Ostrix</span><span>Vantiq</span><span>Seatwise</span><span><i></i>Corban</span>
</div>

<h2 class="quote">"Best program I have ever attended in my career - Rosalie"</h2>

<section class="story">
  <p>Welcome! I am Mei Lan, I am known for helping professionals and executives find clarity in their career and life, so they can focus on what really matters and succeed with joy and meaning.</p>
  <p>In 2008, I was a senior executive with a young family seemingly had it all. However, I felt tired, unhappy and wanted to quit. At the end, I didn't quit, instead I began a search for an answer.</p>
  <p>I did extensive research over the years. What I found is that what I felt is normal and can be turned around with a simple approach.</p>
  <p>The approach gave me the direction, energy, made me a better leader and mum, and took me to a whole new level of joy, success, and career fulfilment. My greatest joy today is enabling others to do the same. <a href="#">Read my search and journey.</a></p>
  <p class="praise">"I know Mei Lan is the best person to guide me on this journey. Mei Lan makes you feel comfortable while pushing you</p>
</section>

<div class="speaker" role="img" aria-label="Photograph of the coach speaking on stage at a seminar"></div>
<p class="caption">Mei Lan Zhou. Executive Coach. Global 100 Exec. Strength Psychology Expert. Mother.</p>
</body>
</html>
```